Honey Label Design (145 × 55 mm) – Premium / Minimal Style

Project Description
I am looking for a professional label design for a 500 g honey jar (twist-off, copper-colored lid).
The design should look premium, elegant, and minimal, reflecting natural quality and regional authenticity.
I expect two design proposals from each designer:

One concept based strictly on my color and style guidelines
One completely free creative concept (designer's own interpretation)

⚠️ Important: The layout and positioning of all elements must follow my specifications exactly (see below). Creativity is welcome in style, colors, and typography—but not in layout structure and content.

Label Size and Constraints

Final size: 145 mm × 55 mm (landscape)
All elements must remain fully within the label area
No part (especially the hexagon) may extend beyond the label boundaries

Design Style

Minimal, clean, premium
No clutter, no excessive colors
Preferred colors:

Warm natural tones (honey, beige, brown)
Inspired by the branding of: www.wabenhof-laden. de
Subtle copper tone accents (to match the lid)

Background

Very subtle illustrated/sketched background
Motif:

Wildflower meadow (foreground)
Mixed forest (background)

Style should be fine line / sketch style, not photorealistic
The background must remain very soft so text remains clearly readable

Central Element (Mandatory)

A hexagon (honeycomb shape) centered on the label
Inside text:

“GERMAN HONEY”
“500 g”

The hexagon must be:

Fully inside the label (no overlapping, my example is wrong)
Visually balanced and centered

Left Text Block (Important)
The following content (in german) must be placed left-aligned (not centered!):
Bottling point:
Henrik Dollmann Beekeeping
Lindenkamper Weg 17
04912 Lindenau
Tel.: 04917 5274061
mail@wabenhof-laden.example
Typography must be clean and clearly structured.

Mandatory White Fields (Very Important)
There must be exactly 3 white boxes:
Size:

Each: 28 mm × 12 mm
No visible border

Positioning (must follow exactly):

Bottom center

Completely blank (for honey type)

Right side – upper field

Text above: “Best before:”

Right side – lower field (directly below)

Text above: “Lot number”

⚠️ All three fields must:

Be identical in size
Be perfectly aligned
Match the layout shown in the reference image

Layout Rules (Strict)

The arrangement of elements is fixed and must not be changed
Center field must be directly below the hexagon
Right-side fields must be vertically aligned
Left text must remain left-aligned

goal
The label should communicate:

High quality / premium honey
Regional trust and authenticity
Clean and professional print-ready design

Reference
A reference image is provided showing:

exact placement of all fields
general layout structure

⚠️ The reference is for layout guidance only — not for copying design style.
Updates

All mandatory information must be in German like the address
Bottling point:
Henrik Dollmann Beekeeping
Lindenkamper W. 17
04912 Lindenau
Tel.: 04917 5274061
www.wabenhof-laden.example

Target Market(s)

Germany

Font styles to use
Sans Serif
Other font styles liked:
• Montserrat, Open Sans, Libre Baskerville

Colors
00AB8E
00BBA5
67D7C9
C6EFE9
E9F9F6
59FF00
82FF00
B8FF75
E3FFCB
F4FFEA
FFF300
FFF600
FEFA6F
FFFEC7
FFFEE8
FFC000
F8CF3A
FAE287
FDF2CF
FEFAEE
F0912C
F2A743
F7CA91
FBE8D2
FDF5EE
EE7325
F08F49
F5BC92
FAE3D3
FDF4ED

Requirements
Must have
• Mandatory Information on Honey Labels (Germany / EU) (Product Name, Country of origin, Net quantity, Minimum durability date (placeholder), Name and address of the food business operator, Batch / lot identification (placeholder), Special warning for infants “Not suitable for infants under 12 months”

```html
<!DOCTYPE html>
<html lang="en">
<head>
<meta charset="utf-8">
<title>German Honey Label</title>
<link rel="stylesheet" href="https://fonts.googleapis.com/css2?family=Cinzel:wght@500;700&family=Marcellus+SC&display=swap">
<style>
  :root {
    --stage: #eeeeee;
    --label-light: #fcefc6;
    --label-mid: #f6dd9c;
    --label-deep: #ecc878;
    --maroon: #8b2f23;
    --field: #fff8e7;
    --hex-fill: #f7e3b0;
    --copper-light: #f3d98a;
    --copper: #c08a3a;
    --copper-dark: #7a5424;
  }
  * { margin: 0; padding: 0; box-sizing: border-box; }
  html, body { width: 1200px; height: 623px; overflow: hidden; background: var(--stage); }
  .label {
    position: absolute; left: 184px; top: 154px; width: 825px; height: 313px;
    overflow: hidden; font-family: "Marcellus SC", serif; color: var(--maroon);
  }
  .landscape {
    position: absolute; inset: 0;
    background:
      radial-gradient(ellipse 60% 45% at 50% 30%, var(--label-light), transparent 70%),
      linear-gradient(180deg, var(--label-light) 0%, var(--label-mid) 55%, var(--label-deep) 100%);
  }
  .brand {
    position: absolute; left: 54px; top: 34px; display: flex; align-items: center; gap: 8px;
    font-size: 18px; letter-spacing: 0.5px; white-space: nowrap;
  }
  .brand-dot { width: 22px; height: 22px; border-radius: 50%; background: var(--maroon); }
  .info { position: absolute; left: 48px; font-size: 13.5px; line-height: 1; white-space: nowrap; }
  .info-heading { top: 99px; }
  .info-row { position: absolute; left: 48px; display: flex; gap: 7px; font-size: 13.5px; white-space: nowrap; }
  .info-row svg { flex: none; width: 11px; height: 11px; margin-top: 1px; fill: var(--maroon); }
  .info-lines { line-height: 17.6px; }
  .row-address { top: 120px; }
  .row-phone { top: 181px; }
  .row-mail { top: 206px; }
  .row-warning { top: 250px; }
  .row-warning .info-lines { line-height: 15px; }
  .row-warning svg { margin-top: 8px; }
  .seal { position: absolute; left: 0; top: 0; width: 825px; height: 313px; }
  .seal-title { font-family: "Cinzel", serif; font-weight: 700; fill: var(--maroon); }
  .seal-weight { font-family: "Cinzel", serif; font-weight: 500; fill: var(--maroon); }
  .field {
    position: absolute; width: 159px; height: 68px; border-radius: 10px; background: var(--field);
  }
  .field-variety { left: 333px; top: 234px; }
  .field-best-before { left: 610px; top: 119px; }
  .field-lot { left: 610px; top: 234px; }
  .field-caption {
    position: absolute; left: 610px; width: 159px; text-align: center; font-size: 13.5px; line-height: 1;
  }
  .caption-best-before { top: 100px; }
  .caption-lot { top: 216px; }
</style>
</head>
<body>
<main class="label">
  <div class="landscape" role="img" aria-label="Soft fine-line sketch of a wildflower meadow in front of a mixed forest and hills, in pale honey tones"></div>

  <div class="brand"><span class="brand-dot"></span>Wabenhof Laden</div>

  <div class="info info-heading">Bottling point:</div>

  <div class="info-row row-address">
    <svg viewBox="0 0 12 12"><path d="M6 0a4.3 4.3 0 0 0-4.3 4.3C1.7 7.5 6 12 6 12s4.3-4.5 4.3-7.7A4.3 4.3 0 0 0 6 0zm0 6a1.7 1.7 0 1 1 0-3.4A1.7 1.7 0 0 1 6 6z"/></svg>
    <div class="info-lines">Henrik Dollmann Beekeeping<br>Lindenkamper Weg 17<br>04912 Lindenau</div>
  </div>

  <div class="info-row row-phone">
    <svg viewBox="0 0 12 12"><path d="M2.4 0.3l1.9 2.4-1 1.4c.7 1.6 2 2.9 3.6 3.6l1.4-1 2.4 1.9-1 2.3C5.4 11 1 6.6.1 1.3z"/></svg>
    <div class="info-lines">Tel.: 04917 5274061</div>
  </div>

  <div class="info-row row-mail">
    <svg viewBox="0 0 12 12"><path d="M0 2h12v1.2L6 6.8 0 3.2zM0 4.6l6 3.6 6-3.6V10H0z"/></svg>
    <div class="info-lines">mail@wabenhof-laden.example</div>
  </div>

  <div class="info-row row-warning">
    <svg viewBox="0 0 12 12"><path d="M6 .5L12 11.5H0zM5.3 4.3v3.8h1.4V4.3zm0 4.7v1.4h1.4V9z"/></svg>
    <div class="info-lines">Not suitable for infants<br>under 12 months</div>
  </div>

  <svg class="seal" viewBox="0 0 825 313" aria-label="German Honey 500 g">
    <defs>
      <linearGradient id="copper-rim" x1="0" y1="0" x2="1" y2="1">
        <stop offset="0" stop-color="var(--copper)"/>
        <stop offset="0.3" stop-color="var(--copper-light)"/>
        <stop offset="0.6" stop-color="var(--copper)"/>
        <stop offset="1" stop-color="var(--copper-dark)"/>
      </linearGradient>
    </defs>
    <polygon points="412.5,16 512,73 512,171 412.5,228 313,171 313,73" fill="url(#copper-rim)"/>
    <polygon points="412.5,25 504,77 504,167 412.5,219 321,167 321,77" fill="var(--maroon)"/>
    <polygon points="412.5,29 500,79 500,165 412.5,215 325,165 325,79" fill="var(--hex-fill)"/>
    <polygon points="412.5,33 496,81 496,163 412.5,211 329,163 329,81" fill="none" stroke="var(--maroon)" stroke-width="1.2"/>
    <text class="seal-title" x="412.5" y="105" text-anchor="middle" font-size="28">GERMAN</text>
    <text class="seal-title" x="415" y="140" text-anchor="middle" font-size="28" letter-spacing="6">HONEY</text>
    <text class="seal-weight" x="412.5" y="175" text-anchor="middle" font-size="20">500G</text>
  </svg>

  <div class="field field-variety"></div>
  <div class="field-caption caption-best-before">Best before:</div>
  <div class="field field-best-before"></div>
  <div class="field-caption caption-lot">Lot number</div>
  <div class="field field-lot"></div>
</main>
</body>
</html>
```